Professional photographer needs website to display and sell images

I'm a nature based travel writer photographer and need a website to sell my wildlife images and perhaps showcase my books.
I also need to upload images and video.
For the books; an author page with bio and a link to my distributor.
My ethos is custodianship of the natural world and I'm appealing to and supporting this mindset to build professional connections and drive sales.

Target Market(s)

Wildlife image sales, ebooks - author promotion, professional connections.

Industry/Entity Type

Photographer

Coding

Coded - Design and coding required

Number of Pages Required

5+ page

Font styles to use
Sans Serif

Colors
2f74b4
6b449b
b768aa
0692cd
ffffff
3277b5
d2a4cc

Requirements
Must have
• Clean uncluttered display for images and easy to navigate pages.
Shop - images for sale
Gallery - upload and delete images
Author page - bio and books
Professional look
Nice to have
• Fade between image displays.
Colour preferences below are a guide.
Should not have
• Slow loading pages, too much text or look too busy.

```html
<!DOCTYPE html>
<html lang="en">
<head>
<meta charset="utf-8">
<title>Heron Field Photography</title>
<link rel="stylesheet" href="https://fonts.googleapis.com/css2?family=Philosopher:wght@400;700&family=Roboto:wght@400;500&display=swap">
<style>
:root{
  --brand:#b05ea4;
  --purple:#6b449b;
  --blue:#2f5fab;
  --text:#222;
  --muted:#6d6d6d;
  --soft:#f4f4f4;
  --dark:#111;
  --white:#fff;
}
*{margin:0;padding:0;box-sizing:border-box}
html,body{width:1200px;height:4827px;overflow:hidden}
body{position:relative;background:var(--white);font-family:'Roboto',sans-serif;color:var(--text)}
.abs{position:absolute}
.heading{font-family:'Philosopher',sans-serif;font-weight:400;color:var(--text)}
.logo{font-family:'Philosopher',sans-serif;font-weight:700;font-size:34px;color:var(--brand)}
.site-header{left:0;top:0;width:1200px;height:72px;background:var(--white)}
.site-header .logo{position:absolute;left:90px;top:14px}
.nav{position:absolute;right:92px;top:25px;display:flex;gap:43px;font-size:15px;color:#555}
.nav .active{color:var(--brand)}
.shapes{left:0;top:0}
.hero-title{left:0;top:305px;width:1200px;text-align:center;font-size:70px;color:var(--white)}
.body-text{font-size:15.5px;line-height:31.3px;color:var(--muted);text-align:justify}
.btn{display:flex;align-items:center;justify-content:center;background:var(--blue);color:var(--white);border-radius:26px;font-size:15px;font-weight:500}
.section-title{font-size:44px}
.card{width:249px;height:290px;border:4px solid var(--purple);top:1671px}
.card-name{width:249px;text-align:center;font-family:'Philosopher',sans-serif;font-size:21px;top:1972px}
.card-price{width:249px;text-align:center;font-size:17px;color:var(--purple);top:2003px}
.arrow{width:44px;height:44px;border-radius:50%;background:var(--white);box-shadow:0 1px 5px rgba(0,0,0,.25);top:1795px;display:flex;align-items:center;justify-content:center}
.tile{overflow:hidden}
.play{position:absolute;left:50%;top:50%;width:60px;height:60px;margin:-30px 0 0 -30px}
.newsletter-text{left:150px;width:900px;text-align:center;font-size:15.5px;line-height:26px;color:var(--muted);top:4140px}
.subscribe-form{left:206px;top:4226px;width:792px;height:51px;border:1px solid #ddd;border-radius:26px;overflow:hidden}
.subscribe-form .field{position:absolute;left:26px;top:16px;font-size:13.5px;color:#888}
.subscribe-form .btn{position:absolute;right:0;top:0;width:190px;height:51px;border-radius:0 26px 26px 0}
.footer-col h4{font-family:'Philosopher',sans-serif;font-weight:400;font-size:21px;color:var(--white);margin-bottom:16px}
.footer-col li{list-style:none;font-size:14px;color:var(--white);line-height:24.4px;display:flex;align-items:center;gap:12px}
.dot{width:9px;height:9px;border-radius:2px;background:var(--white)}
.footer-about{left:90px;top:4572px;width:412px;font-size:13.5px;line-height:24px;color:var(--white);text-align:justify}
.copyright{left:0;top:4791px;width:1200px;text-align:center;font-size:13px;color:var(--white)}
</style>
</head>
<body>

<svg class="abs shapes" width="1200" height="4827" viewBox="0 0 1200 4827" aria-hidden="true">
  <path d="M0,1459 Q600,1579 1200,1459 L1200,2175 Q600,2063 0,2175 Z" fill="#f4f4f4"/>
  <path d="M0,4378 Q600,4510 1200,4378 L1200,4827 L0,4827 Z" fill="#111"/>
  <circle cx="339" cy="2529" r="250" fill="#6b449b"/>
  <circle cx="178" cy="2334" r="88" fill="#6b449b"/>
</svg>

<header class="abs site-header">
  <div class="logo">Heron Field Photography</div>
  <nav class="nav">
    <span class="active">Home</span><span>About Us</span><span>Videos</span><span>Gallery</span><span>Blog</span><span>Contact Us</span>
  </nav>
</header>

<section class="hero">
  <div class="abs" role="img" aria-label="Monochrome photograph of a large seabird in flight over dark foliage" style="left:0;top:72px;width:1200px;height:650px;background:radial-gradient(ellipse at 50% 35%,#6a6a6a 0%,#2e2e2e 45%,#141414 100%)"></div>
  <svg class="abs" style="left:0;top:580px" width="1200" height="150" viewBox="0 580 1200 150" aria-hidden="true">
    <path d="M0,722 Q600,590 1200,722 L1200,730 L0,730 Z" fill="#fff"/>
  </svg>
  <h1 class="abs heading hero-title">Real World Images</h1>
</section>

<section class="about">
  <h2 class="abs heading section-title" style="left:90px;top:915px">About Me</h2>
  <p class="abs body-text" style="left:90px;top:984px;width:473px">Lorem ipsum dolor sit amet, consectetur adipiscing elit, sed do eiusmod tempor incididunt ut labore et dolore magna aliqua. Ut enim ad minim veniam, quis nostrud exercitation ullamco laboris nisi ut aliquip ex ea commodo consequat. Duis aute irure dolor in reprehenderit in voluptate velit esse cillum dolore eu fugiat nulla pariatur. Excepteur sint occaecat cupidatat non proident, sunt in culpa qui officia deserunt mollit anim id est laborum.</p>
  <div class="abs btn" style="left:90px;top:1240px;width:180px;height:51px">Read More</div>
  <div class="abs" role="img" aria-label="Photograph of a seabird gliding low over deep blue water" style="left:607px;top:858px;width:500px;height:500px;border-radius:50%;background:radial-gradient(circle at 45% 45%,#2f5f92,#183f6c 70%,#102c50)"></div>
  <div class="abs" style="left:920px;top:825px;width:188px;height:188px;border-radius:50%;background:var(--purple)"></div>
</section>

<section class="products">
  <h2 class="abs heading section-title" style="left:0;top:1605px;width:1200px;text-align:center">Products</h2>
  <div class="abs card" role="img" aria-label="Photograph of a tern in flight against a pale sky" style="left:90px;background:#b3c8df"></div>
  <div class="abs card" role="img" aria-label="Photograph of a swallow perched on a wire" style="left:347px;background:linear-gradient(#2f4f78,#3f6590)"></div>
  <div class="abs card" role="img" aria-label="Photograph of a bee-eater in flight" style="left:604px;background:#8aa7cc"></div>
  <div class="abs card" role="img" aria-label="Photograph of a gull in flight against blue sky" style="left:861px;background:#2b74c0"></div>
  <div class="abs card-name" style="left:90px">Product Name</div>
  <div class="abs card-name" style="left:347px">Product Name</div>
  <div class="abs card-name" style="left:604px">Product Name</div>
  <div class="abs card-name" style="left:861px">Product Name</div>
  <div class="abs card-price" style="left:90px">$20.00</div>
  <div class="abs card-price" style="left:347px">$20.00</div>
  <div class="abs card-price" style="left:604px">$20.00</div>
  <div class="abs card-price" style="left:861px">$20.00</div>
  <div class="abs arrow" style="left:68px"><svg width="12" height="12" viewBox="0 0 12 12"><path d="M8 2 L4 6 L8 10" fill="none" stroke="#555" stroke-width="1.5"/></svg></div>
  <div class="abs arrow" style="left:1086px"><svg width="12" height="12" viewBox="0 0 12 12"><path d="M4 2 L8 6 L4 10" fill="none" stroke="#555" stroke-width="1.5"/></svg></div>
</section>

<section class="books">
  <div class="abs" role="img" aria-label="Book cover with a tree silhouetted against a golden sunset" style="left:195px;top:2291px;width:289px;height:503px;background:linear-gradient(160deg,#e8c060 0%,#b07a2a 40%,#2a2010 80%,#111 100%);box-shadow:6px 6px 12px rgba(0,0,0,.3)"></div>
  <h2 class="abs heading section-title" style="left:630px;top:2338px">My Books</h2>
  <p class="abs body-text" style="left:630px;top:2406px;width:475px">Lorem ipsum dolor sit amet, consectetur adipiscing elit, sed do eiusmod tempor incididunt ut labore et dolore magna aliqua. Ut enim ad minim veniam, quis nostrud exercitation ullamco laboris nisi ut aliquip ex ea commodo consequat. Duis aute irure dolor in reprehenderit in voluptate velit esse cillum dolore eu fugiat nulla pariatur. Excepteur sint occaecat cupidatat non proident, sunt in culpa qui officia deserunt mollit anim id est laborum.</p>
  <div class="abs btn" style="left:630px;top:2662px;width:180px;height:51px">Buy Now</div>
</section>

<section class="media">
  <h2 class="abs heading section-title" style="left:90px;top:2897px">Images &amp; Video</h2>
  <div class="abs btn" style="left:928px;top:2902px;width:178px;height:51px;gap:8px">
    <svg width="14" height="14" viewBox="0 0 14 14"><path d="M7 1 L3 5 H5.5 V9 H8.5 V5 H11 Z M2 11 H12 V13 H2 Z" fill="#fff"/></svg>Upload
  </div>
  <div class="abs tile" role="img" aria-label="Photograph of waves at golden sunset" style="left:90px;top:2976px;width:266px;height:243px;background:linear-gradient(#e9b23c,#7a5a28 60%,#2e2a22)"></div>
  <div class="abs tile" role="img" aria-label="Video still of sunlight through forest trees" style="left:358px;top:2976px;width:482px;height:243px;background:linear-gradient(#cfd6c8,#3c4f2e 45%,#1f2c18)">
    <svg class="play" viewBox="0 0 60 60"><circle cx="30" cy="30" r="27" fill="none" stroke="#fff" stroke-width="3"/><path d="M24 18 L42 30 L24 42 Z" fill="#fff"/></svg></div>
  <div class="abs tile" role="img" aria-label="Photograph of a motorcycle dashboard on a country road" style="left:844px;top:2976px;width:266px;height:493px;background:linear-gradient(#4f86c6,#8a9aa8 35%,#2a2e33 65%,#15181b)"></div>
  <div class="abs tile" role="img" aria-label="Video still of a bird swimming in turquoise water" style="left:90px;top:3225px;width:482px;height:244px;background:linear-gradient(#2f9aa8,#4fb3bd 50%,#2a8d9b)">
    <svg class="play" viewBox="0 0 60 60"><circle cx="30" cy="30" r="27" fill="none" stroke="#fff" stroke-width="3"/><path d="M24 18 L42 30 L24 42 Z" fill="#fff"/></svg></div>
  <div class="abs tile" role="img" aria-label="Photograph of a dragonfly on a flower" style="left:576px;top:3225px;width:264px;height:244px;background:radial-gradient(circle,#b49a4a,#1e3318 65%)"></div>
  <div class="abs tile" role="img" aria-label="Photograph of pelicans on dark water" style="left:90px;top:3474px;width:266px;height:494px;background:linear-gradient(#2a4a2a,#16261c 50%,#0f1a22)"></div>
  <div class="abs tile" role="img" aria-label="Video still of an eagle in flight over trees" style="left:360px;top:3474px;width:480px;height:244px;background:linear-gradient(#3a5a3a,#203a26)">
    <svg class="play" viewBox="0 0 60 60"><circle cx="30" cy="30" r="27" fill="none" stroke="#fff" stroke-width="3"/><path d="M24 18 L42 30 L24 42 Z" fill="#fff"/></svg></div>
  <div class="abs tile" role="img" aria-label="Photograph of a light at night" style="left:844px;top:3474px;width:266px;height:244px;background:radial-gradient(circle at 35% 45%,#888,#222 30%,#111)"></div>
  <div class="abs tile" role="img" aria-label="Photograph of a reed stem with a night light" style="left:360px;top:3724px;width:264px;height:244px;background:radial-gradient(circle at 25% 30%,#aaa,#2a2e1a 25%,#121510)"></div>
  <div class="abs tile" role="img" aria-label="Video still of a colourful bird among flowers" style="left:628px;top:3724px;width:482px;height:244px;background:linear-gradient(120deg,#6a7a4a,#a86a5a 45%,#4a6a5a)">
    <svg class="play" viewBox="0 0 60 60"><circle cx="30" cy="30" r="27" fill="none" stroke="#fff" stroke-width="3"/><path d="M24 18 L42 30 L24 42 Z" fill="#fff"/></svg></div>
</section>

<section class="newsletter">
  <h2 class="abs heading section-title" style="left:0;top:4075px;width:1200px;text-align:center">Subscribe Our Newsletter</h2>
  <p class="abs newsletter-text">Lorem ipsum dolor sit amet, consectetur adipiscing elit, sed do eiusmod tempor incididunt ut labore et dolore magna aliqua.<br>Ut enim ad minim veniam, quis nostrud exercitation ullamco laboris nisi ut aliquip ex ea commodo consequat.</p>
  <div class="abs subscribe-form">
    <span class="field">Enter Your Email Address</span>
    <div class="btn">Subscribe</div>
  </div>
</section>

<footer>
  <div class="abs logo" style="left:90px;top:4506px">Heron Field Photography</div>
  <p class="abs footer-about">Lorem ipsum dolor sit amet, consectetur adipiscing elit, sed do eiusmod tempor incididunt ut labore et dolore magna aliqua. Ut enim ad minim veniam, quis nostrud exercitation ullamco laboris nisi ut aliquip ex ea commodo consequat.</p>
  <div class="abs footer-col" style="left:653px;top:4516px">
    <h4>Links</h4>
    <ul><li>Home</li><li>About Us</li><li>Videos</li><li>Gallery</li><li>Blog</li><li>Contact Us</li></ul>
  </div>
  <div class="abs footer-col" style="left:833px;top:4516px">
    <h4>Others</h4>
    <ul><li>FAQ</li><li>Books</li><li>Products</li></ul>
  </div>
  <div class="abs footer-col" style="left:1009px;top:4516px">
    <h4>Follow Us</h4>
    <ul><li><span class="dot"></span>Community</li><li><span class="dot"></span>Updates</li><li><span class="dot"></span>Photo Feed</li><li><span class="dot"></span>Video Channel</li></ul>
  </div>
  <div class="abs copyright">Copyrights © 2021, The Company Name. All rights reserved.</div>
</footer>

</body>
</html>
```